Webbanner-Design für Webradio Moderator
Zielgruppe
Ich bin ein Webradio Moderator. Ich unterhalte die Zuhörer mit einem bunten Music Mix und Ihren Wünschen.
Die Zielgruppe sind Leute die mein Werbe Banner dann sehen und Anhand dessen zu unserm Webradio kommen und uns zuhören.
I'm a Webradio moderator. I'm entertaining the audience with a colorful music mix and your wishes.
The target group are people who see my advertising banner and then come to our own Webradio and listen to us.
Aufgabenstellung
Es sollte so gestaltet sein, dass man genau weis um was es geht.
Eine gute Mischung das es nicht zu viel Bild neben dem Text ist aber auch nicht zu wenig.
Es sollte im Style wie der Banner 'wildtommi_show.jpg' unten etwa sein.
It should be designed to be exactly a point about what it is.
A good mix that does not take too much image next to the text is not too little.
It should be at the style like the banner'wildtommi _ show. jpg down.

```html
<!DOCTYPE html>
<html lang="de">
<head>
<meta charset="utf-8">
<title>Wild Tommi – On Air</title>
<link rel="stylesheet" href="https://fonts.googleapis.com/css2?family=Anton&family=Roboto+Condensed:wght@700&family=Nunito:wght@900&display=swap">
<style>
  :root {
    --bg: #050505;
    --warm-1: #c8501a;
    --warm-2: #8a1a12;
    --cool-1: #1a8fb0;
    --cool-2: #2a2fa8;
    --cool-3: #5a2090;
    --white: #ffffff;
    --sign-frame: #3a3a3a;
    --sign-face: #0b0b0b;
    --sign-red: #ff2a1a;
    --btn-top: #9be23a;
    --btn-bottom: #3f9e12;
    --btn-edge: #2d7a0c;
  }
  html, body {
    margin: 0;
    padding: 0;
    width: 1200px;
    height: 676px;
    overflow: hidden;
    background: var(--bg);
  }
  .banner {
    position: relative;
    width: 1200px;
    height: 676px;
    overflow: hidden;
    background: var(--bg);
  }
  .sound-burst {
    position: absolute;
    inset: 0;
    background:
      radial-gradient(ellipse 38% 60% at 50% 50%, rgba(5,5,5,0.95) 30%, rgba(5,5,5,0) 100%),
      linear-gradient(90deg, var(--warm-2) 0%, var(--warm-1) 25%, #1a0e08 48%, #06101a 55%, var(--cool-1) 75%, var(--cool-2) 90%, var(--cool-3) 100%);
  }
  .on-air-sign {
    position: absolute;
    left: 468px;
    top: 10px;
    width: 248px;
    height: 90px;
    box-sizing: border-box;
    border: 8px solid var(--sign-frame);
    border-radius: 4px;
    background: var(--sign-face);
    display: flex;
    align-items: center;
    justify-content: center;
  }
  .on-air-sign__label {
    font-family: "Roboto Condensed", sans-serif;
    font-weight: 700;
    font-size: 50px;
    letter-spacing: 2px;
    color: var(--sign-red);
    text-shadow: 0 0 10px rgba(255,40,20,0.8);
  }
  .host-name {
    position: absolute;
    left: 0;
    width: 1200px;
    text-align: center;
    font-family: "Anton", sans-serif;
    font-weight: 400;
    color: var(--white);
    line-height: 1;
    margin: 0;
    letter-spacing: 6px;
  }
  .host-name--first { top: 98px; font-size: 175px; }
  .host-name--last { top: 238px; font-size: 230px; transform: scaleX(0.85); }
  .play-button {
    position: absolute;
    left: 360px;
    top: 496px;
    width: 490px;
    height: 90px;
    box-sizing: border-box;
    border-radius: 12px;
    border: 3px solid var(--btn-edge);
    background: linear-gradient(180deg, var(--btn-top) 0%, #6cc424 50%, var(--btn-bottom) 100%);
    box-shadow: inset 0 2px 0 rgba(255,255,255,0.5);
    display: flex;
    align-items: center;
  }
  .play-button__icon {
    position: absolute;
    left: 24px;
    top: 20px;
  }
  .play-button__label {
    width: 100%;
    text-align: center;
    padding-left: 40px;
    font-family: "Roboto Condensed", sans-serif;
    font-weight: 700;
    font-size: 48px;
    color: var(--white);
    text-shadow: 0 2px 3px rgba(0,0,0,0.55);
  }
  .station-url {
    position: absolute;
    left: 0;
    top: 606px;
    width: 1200px;
    text-align: center;
    font-family: "Nunito", sans-serif;
    font-weight: 900;
    font-size: 44px;
    color: var(--white);
    margin: 0;
  }
</style>
</head>
<body>
  <main class="banner">
    <div class="sound-burst" role="img" aria-label="Hintergrundbild: leuchtende Schallwellen in Orange links und Blau-Violett rechts"></div>

    <div class="on-air-sign"><span class="on-air-sign__label">ON AIR</span></div>

    <h1 class="host-name host-name--first">WILD</h1>
    <p class="host-name host-name--last">TOMMI</p>

    <div class="play-button">
      <svg class="play-button__icon" width="44" height="46" viewBox="0 0 44 46" aria-hidden="true">
        <polygon points="4,2 42,23 4,44" fill="#ffffff"/>
      </svg>
      <span class="play-button__label">PLAY NOW</span>
    </div>

    <p class="station-url">www.dieblauewellesound.example</p>
  </main>
</body>
</html>
```